Promotional Flyer for "Veranto events" with LOGO DESIGN

I am developing my own start-up company which is organising and managing exclusive and luxury events in Vienna, London, and Venice. Elegant promotional flyer should introduce and promote my company to a broad spectrum of high level clients; both online and by regular hardcopy post. This flyer should reflect the highest level of elegance, professionalism, creativity, sophistication, and exclusivity as well as irradiating a feeling of child like joy . I want the flyer to be two sided or folded, but did not find that version. It should be including the photo from the main page of the site "www.veranto-events.example". Text should contain the following :
Creative ideas and event concept
Unique venue selection
Complete planning and coordination
First class catering
Professional photography and video productions ---
--------------------------------------------------------------------
1.Surprise the unsurprisable
2. we materialise your innermost dreams into trend setting entertainment and unique celebration of any occasion
------------------------------------------------------------------------
You can take ideas from any photo on my website, I also add some additional photos
I am available via e-mail or phone +393471926604 /+447513064287. Thank you.

Target Market(s)

high level discreet and the discerning client with taste, well travelled already spoiled

Industry/Entity Type

Event Planning

Font styles to use
Sans Serif

Colors
ffffff
fffbf0

Requirements
Must have
• unexpected simlicity, be extremely different from all what is there on the market
Should not have
• eye catching and memorable yet not too busy

```html
<!DOCTYPE html>
<html lang="en">
<head>
<meta charset="utf-8">
<title>Veranto events – flyer front and back</title>
<link rel="stylesheet" href="https://fonts.googleapis.com/css2?family=Bree+Serif&family=Roboto+Condensed:wght@400;700&display=swap">
<style>
  :root {
    --stage: #b9b9b9;
    --brown-dark: #4a2a12;
    --brown: #6b3d1a;
    --ink: #1e1208;
    --amber-light: #f6dca6;
    --amber: #e2a24e;
    --amber-deep: #a8672a;
    --cream: #fffbf0;
    --white: #ffffff;
    --leaf-light: #eef5d6;
    --leaf: #a9d35a;
    --leaf-deep: #6fae2a;
    --frame: #5a3416;
  }
  * { box-sizing: border-box; margin: 0; padding: 0; }
  html, body { width: 1200px; height: 900px; overflow: hidden; }
  body {
    position: relative;
    background: var(--stage);
    font-family: "Roboto Condensed", "Arial Narrow", sans-serif;
    color: var(--ink);
  }

  .flyer { position: absolute; overflow: hidden; }
  .flyer--front { left: 77px; top: 128px; width: 492px; height: 694px; }
  .flyer--back  { left: 618px; top: 130px; width: 488px; height: 690px; }

  .flyer__photo { position: absolute; inset: 0; }
  .flyer--front .flyer__photo {
    background:
      radial-gradient(ellipse 42% 30% at 40% 47%, #f3c85a 0%, #c98a2c 55%, transparent 80%),
      linear-gradient(160deg, #d99a4c 0%, var(--amber-light) 45%, #e9c48c 75%, #f3dfbe 100%);
  }
  .flyer--back .flyer__photo {
    background:
      radial-gradient(ellipse 40% 55% at 42% 45%, rgba(255,246,236,0.95) 0%, rgba(245,232,214,0.8) 50%, transparent 80%),
      linear-gradient(100deg, var(--leaf-light) 0%, #f4eedd 35%, #d8e9a6 65%, var(--leaf) 85%, var(--leaf-deep) 100%);
  }

  .flyer__bands { position: absolute; inset: 0; width: 100%; height: 100%; }

  .brand {
    position: absolute;
    display: flex; align-items: center; gap: 10px;
    font-family: "Bree Serif", Georgia, serif;
    font-size: 31px; letter-spacing: 1px;
    text-transform: uppercase;
    color: var(--brown);
    white-space: nowrap;
  }
  .brand__mark { width: 14px; height: 14px; border-radius: 50%; background: var(--brown); }
  .flyer--front .brand { left: 130px; top: 222px; }
  .flyer--back .brand  { left: 27px;  top: 220px; }

  .headline {
    position: absolute;
    font-family: "Bree Serif", Georgia, serif;
    font-weight: 400; font-size: 22px;
    color: var(--brown-dark);
    text-transform: uppercase;
    white-space: nowrap;
  }
  .flyer--front .headline { left: 123px; top: 274px; }
  .flyer--back .headline  { left: 27px;  top: 270px; }

  .promise {
    position: absolute; right: 31px; top: 322px; width: 360px;
    text-align: right; font-size: 17px; line-height: 22.5px;
  }

  .cities {
    position: absolute; left: 28px; right: 35px; top: 518px;
    display: flex; justify-content: space-between;
    font-family: "Bree Serif", Georgia, serif; font-size: 24px;
    color: var(--ink); list-style: none;
  }

  .gallery { position: absolute; display: flex; gap: 8px; }
  .flyer--front .gallery { left: 25px; top: 558px; }
  .flyer--back .gallery  { left: 27px; top: 556px; }
  .gallery__item {
    width: 140px; height: 84px;
    border: 2px solid var(--frame); border-radius: 6px;
  }
  .flyer--back .gallery__item { width: 138px; }
  .gallery__item--candles  { background: linear-gradient(135deg, #3a2412, #b7742c 55%, #2b190c); }
  .gallery__item--costume  { background: linear-gradient(135deg, #5a2a10, #d0752a 50%, #7a3a14); }
  .gallery__item--stage    { background: linear-gradient(135deg, #4a2a20, #d8b6a0 50%, #6a3a2a); }
  .gallery__item--garden   { background: linear-gradient(180deg, #cfe0c0, #e9ecef 45%, #5f9a3a); }
  .gallery__item--table    { background: linear-gradient(135deg, #6e8a3a, #e88a3a 50%, #c4502a); }
  .gallery__item--show     { background: linear-gradient(135deg, #1c1d5a, #9a7ad0 50%, #2a2a70); }

  .site-link {
    position: absolute; left: 0; right: 0; top: 662px;
    text-align: center; font-size: 13px; color: var(--ink);
  }

  .services {
    position: absolute; left: 27px; top: 306px;
    list-style: none; font-size: 17.5px; line-height: 30.5px;
  }
  .services li { display: flex; align-items: center; gap: 9px; }
  .services li::before {
    content: ""; width: 7px; height: 7px; border-radius: 50%;
    background: var(--ink); flex: none;
  }

  .contact__title {
    position: absolute; left: 44px; top: 466px;
    font-family: "Bree Serif", Georgia, serif; font-size: 15px;
    color: var(--brown-dark); text-transform: uppercase; font-weight: 400;
  }
  .contact__phones, .contact__online {
    position: absolute; font-size: 13px; line-height: 17px; list-style: none;
  }
  .contact__phones { left: 27px; top: 491px; }
  .contact__online { left: 240px; top: 490px; }
  .contact__phones li, .contact__online li { display: flex; align-items: center; gap: 4px; }
  .contact__phones li:not(:first-child) { padding-left: 15px; }
  .icon { width: 12px; height: 12px; flex: none; }
</style>
</head>
<body>

<section class="flyer flyer--front" aria-label="Flyer front">
  <div class="flyer__photo" role="img" aria-label="Warm close-up of an antique brass compass resting among wine corks"></div>
  <svg class="flyer__bands" viewBox="0 0 492 694" aria-hidden="true">
    <polygon points="0,150 240,0 492,0 492,60 0,370" fill="#fff" opacity="0.18"/>
    <polygon points="150,0 492,250 492,470 0,110 0,0" fill="#fff" opacity="0.14"/>
    <polygon points="90,290 492,20 492,330 260,520" fill="#fffbf0" opacity="0.45"/>
    <polygon points="0,470 210,694 0,694" fill="#fff" opacity="0.2"/>
    <polygon points="492,420 300,694 492,694" fill="#fff" opacity="0.2"/>
  </svg>

  <div class="brand"><span class="brand__mark"></span>Veranto Events</div>
  <h1 class="headline">Surprise the unsurprisable</h1>
  <p class="promise">Your innermost dreams materialised into trend setting entertainment and unique celebration of any occasion.</p>

  <ul class="cities">
    <li>Venice</li><li>London</li><li>Vienna</li><li>Moscow</li>
  </ul>

  <div class="gallery">
    <div class="gallery__item gallery__item--candles" role="img" aria-label="Two children holding candles in the dark"></div>
    <div class="gallery__item gallery__item--costume" role="img" aria-label="Guests in historical costume at a candlelit ball"></div>
    <div class="gallery__item gallery__item--stage" role="img" aria-label="Performers in baroque gowns and wigs on stage"></div>
  </div>

  <p class="site-link">www.veranto-events.example</p>
</section>

<section class="flyer flyer--back" aria-label="Flyer back">
  <div class="flyer__photo" role="img" aria-label="Young girl taking a photograph with a compact camera against a green meadow"></div>
  <svg class="flyer__bands" viewBox="0 0 488 690" aria-hidden="true">
    <polygon points="0,0 120,0 488,260 488,420 0,60" fill="#fff" opacity="0.22"/>
    <polygon points="0,330 400,0 488,0 488,90 0,470" fill="#fff" opacity="0.25"/>
    <polygon points="0,170 360,420 0,640" fill="#fffbf0" opacity="0.35"/>
    <polygon points="488,430 260,690 488,690" fill="#fff" opacity="0.25"/>
  </svg>

  <div class="brand"><span class="brand__mark"></span>Veranto Events</div>
  <h2 class="headline">What we do</h2>
  <ul class="services">
    <li>Creative ideas and event concept</li>
    <li>Unique venue selection</li>
    <li>Complete planning and coordination</li>
    <li>First class catering</li>
    <li>Professional photography and video productions</li>
  </ul>

  <h3 class="contact__title">Contact us:</h3>
  <ul class="contact__phones">
    <li>
      <svg class="icon" viewBox="0 0 24 24" aria-hidden="true"><path d="M6.6 10.8a15 15 0 0 0 6.6 6.6l2.2-2.2a1 1 0 0 1 1-.25 11.4 11.4 0 0 0 3.6.57 1 1 0 0 1 1 1V20a1 1 0 0 1-1 1A17 17 0 0 1 3 4a1 1 0 0 1 1-1h3.5a1 1 0 0 1 1 1c0 1.25.2 2.45.57 3.57a1 1 0 0 1-.25 1z" fill="#1e1208"/></svg>
      +393471926604
    </li>
    <li>+447513064287</li>
    <li>+447700900418</li>
  </ul>
  <ul class="contact__online">
    <li>
      <svg class="icon" viewBox="0 0 24 24" aria-hidden="true"><circle cx="12" cy="12" r="10" fill="#1e1208"/><path d="M2 12h20M12 2c3 3 3 17 0 20M12 2c-3 3-3 17 0 20" stroke="#fffbf0" stroke-width="1.5" fill="none"/></svg>
      www.veranto-events.example
    </li>
    <li>
      <svg class="icon" viewBox="0 0 24 24" aria-hidden="true"><rect x="2" y="5" width="20" height="14" fill="none" stroke="#1e1208" stroke-width="2"/><path d="M2 5l10 8 10-8" fill="none" stroke="#1e1208" stroke-width="2"/></svg>
      marketing@veranto-events.example
    </li>
  </ul>

  <div class="gallery">
    <div class="gallery__item gallery__item--garden" role="img" aria-label="Bride and bridesmaids in white on a garden lawn"></div>
    <div class="gallery__item gallery__item--table" role="img" aria-label="Candlelit table decorated with orange flowers"></div>
    <div class="gallery__item gallery__item--show" role="img" aria-label="Dancer with wide winged costume under violet stage light"></div>
  </div>
</section>

</body>
</html>
```